Stationery Design for Pfotenhaus

We already have a logo a Logo for our outstanding veterinary hospital. Now we are looking for our future letterhead, business cards and envelopes. We would like to see a design using the color from our logo. Additional color should be limited to grey or a rusty brown. The font should be easy and clearly readable and must be easily available on all computers (to install it in our Management software). The finial design should communicate competence in veterinary medicine, and empathy.

To meet the European regulation (DIN5008) there are a couple mandatory legal informations one the letterhead. We also enclosed a template of exact measurement, which need to be respected according to DIN5008.

Mandatory legal information are (best placed in the footer):
"Pfotenhaus GmbH & Co KG, Brunnfeldgasse 417C, 1140 Wien,
Handelsgericht Wien, FN 294617k, GF: Dr. Lorenz Haidinger
ATU 3918462"
Additional informations needed:
"Tel: +43 1 5849162, Fax: +43 1 5849163, info@pfotenhaus-demo.at, www. pfotenhaus-demo.at"
bank account informations should be included as well. These are:
"Sparkasse Hollental Nord, IBAN: AT 58 1111 2222 3333 4444, BIC: HLNTAT2H517"

The Logo should be in the upper right corner. Below that we need a space for informations regarding the responsible veterinarians. There will be 3-5 Names, each of it consisting of 2 lines (see example below). The Names should be highlighted (larger font) compared to the qualifications in the second line.
Tierärztliche Leitung:
Dr. Lorenz Haidinger
Diplomate ECVS
Updates

The contest was startet on the 2nd of may and the deadline was a day later? Why was that so fast? Did I do something wrong? BR

Target Market(s)

dog and cat owner in Austria as welle as referring veterinarians in Austria

Industry/Entity Type

Veterinary

Contact Information for Business Card

One side: Logo
other side:
Dr. Lorenz Haidinger
Diplomate ECVS
EBVS Specialist of Small Animal Surgery

Pfotenhaus GmbH&Co KG
Brunnfeldgasse 417C
1140 Wien

Tel: +43 1 5849160 DW 102
Fax: +43 1 5849160 DW 999
email: lorenz.haidinger@pfotenhaus-demo.at

Font styles to use
Serif
Sans Serif

Requirements
Must have
• The logo should be given in the upper right. Most of the legal informations should be given in the footer. The upper left Area should be clear, since the recipient address will be placed there.
Colors should be limited to golden, blue and greyscale (two different gereysacales at most).

```html
<!DOCTYPE html>
<html lang="de">
<head>
<meta charset="utf-8">
<title>Pfotenhaus Briefpapier</title>
<link href="https://fonts.googleapis.com/css2?family=Poppins:wght@400;500;600&family=Didact+Gothic&display=swap" rel="stylesheet">
<style>
  :root{
    --navy:#17284f;
    --gold:#e0a928;
    --ink:#2a2a2a;
    --grey:#555;
    --paper:#ececec;
    --backdrop:#c2c2c2;
  }
  *{margin:0;padding:0;box-sizing:border-box}
  html,body{width:960px;height:1200px;overflow:hidden;background:var(--backdrop)}
  .sheet{position:absolute;left:52px;top:0;width:855px;height:1200px;
    background:linear-gradient(90deg,#f1f1f1,#e4e4e4);font-family:"Didact Gothic",sans-serif;color:var(--ink)}
  .brand{position:absolute;right:78px;top:54px;text-align:right}
  .brand-mark{display:block;width:80px;height:80px;border-radius:50%;background:var(--navy);
    border:3px solid var(--gold);margin:0 6px 10px auto}
  .brand-name{font-family:"Poppins",sans-serif;font-weight:600;font-size:27px;color:var(--navy);line-height:1}
  .brand-tag{font-family:"Poppins",sans-serif;font-weight:500;font-size:12px;color:var(--gold);margin-top:3px}
  .management{position:absolute;right:80px;top:196px;text-align:right;font-family:"Poppins",sans-serif}
  .management h2{font-size:14px;font-weight:500;color:var(--navy);margin-bottom:3px}
  .vet{margin-bottom:6px}
  .vet-name{font-size:13.5px;color:var(--gold);line-height:1.15}
  .vet-title{font-size:10px;color:var(--grey);line-height:1.2}
  .recipient{position:absolute;left:120px;top:242px;font-size:13.5px;line-height:17px}
  .recipient .ref{margin-top:31px}
  .letter{position:absolute;left:136px;top:434px;width:590px}
  .salutation{font-size:20px;margin-bottom:34px}
  .letter p{font-size:12.4px;line-height:18.3px;text-align:justify;margin-bottom:18px}
  .closing{margin-top:36px;font-size:12.4px}
  .signature{display:block;width:115px;height:65px;margin:10px 0 0 22px;
    background:linear-gradient(90deg,#d6d6d6,#cfcfcf);border-radius:4px}
  .footer{position:absolute;left:76px;top:1063px;width:706px;height:72px;
    border-top:1px solid #222;border-bottom:1px solid #222;text-align:center;
    font-family:"Poppins",sans-serif;font-size:10px;color:#444;padding-top:10px;line-height:17px}
  .footer .co{color:var(--navy)}
  .footer svg{width:9px;height:9px;vertical-align:-1px;fill:var(--navy)}
  .band{position:absolute;left:-6px;right:0;bottom:0;height:18px;background:var(--navy)}
</style>
</head>
<body>
<div class="sheet">
  <header class="brand">
    <span class="brand-mark"></span>
    <div class="brand-name">Pfotenhaus</div>
    <div class="brand-tag">Fachklinik für Kleintiere</div>
  </header>

  <section class="management">
    <h2>Tierärztliche Leitung</h2>
    <div class="vet"><div class="vet-name">Dr. Lorenz Haidinger</div><div class="vet-title">Diplomate ECVS</div></div>
    <div class="vet"><div class="vet-name">Dr. Jonas Feldner</div><div class="vet-title">Diplomate ECVS</div></div>
    <div class="vet"><div class="vet-name">Dr. Mirela</div><div class="vet-title">Diplomate ECVS</div></div>
  </section>

  <address class="recipient" style="font-style:normal">
    <div>Vivamus faucibus, ipsum nec<br>aliquet viverra, leo mauris condime</div>
    <div class="ref">faucibuspsum</div>
  </address>

  <main class="letter">
    <div class="salutation">Dear Mr. Falkner,</div>
    <p>Lorem ipsum dolor sit amet, consectetur adipiscing elit. Donec orci purus, luctus vitae dignissim eu, iaculis sed purus. Vivamus faucibus, ipsum nec aliquet viverra, leo mauris condimentum ligula, sit amet sagittis enim ligula quis arcu. Nam egestas tortor id nisi porttitor mattis. In tortor ante, ultricies in suscipit a, tempus non massa. Vivamus et auctor mi. Fusce vel massa nulla. Phasellus nec eros mauris, et scelerisque orci.</p>
    <p>Donec malesuada orci vitae nulla accumsan porta a id massa. Quisque accumsan iaculis magna sit amet fringilla. Maecenas consequat, magna eget tincidunt semper, odio nibh rutrum mi, id feugiat ante nisi eu risus. Vestibulum nunc orci, rhoncus a placerat in, ultricies in mi. Cras mattis varius eros, vel fringilla nisi suscipit eget. Quisque scelerisque sagittis nulla at porttitor.</p>
    <p>Sed id augue vitae urna euismod commodo aliquet a quam. Pellentesque arcu velit, cursus et malesuada ut, consequat et diam. Nullam erat sem, rhoncus id ullamcorper vitae, rhoncus et arcu. In ultricies ultricies nulla, ut rutrum nisi iaculis at. Donec eu magna a metus ornare faucibus. Fusce aliquet faucibus ultricies. Morbi semper, est id tincidunt gravida, sem arcu adipiscing lacus, ac bibendum nulla leo eu purus. Quisque nec diam sed risus consectetur a ccumsan quis quis nibh. Vestibulum id purus lorem.</p>
    <p>It is a long established fact that a reader will be distracted by the readable content of a page when looking at its layout. The point of using Lorem Ipsum is that it has a more-or-less normal distribution of letters, as opposed to using 'Content here, content here', making it look like readable English. Many desktop publishing packages</p>
    <div class="closing">Sincerely,</div>
    <span class="signature" role="img" aria-label="Handwritten signature"></span>
  </main>

  <footer class="footer">
    <div><span class="co">Pfotenhaus GmbH &amp; Co KG</span>, Brunnfeldgasse 417C, 1140 Wien, Handelsgericht Wien, FN 294617k</div>
    <div>
      <svg viewBox="0 0 10 10"><path d="M2 0.5l2 2-1 1.2c.6 1.3 1.7 2.4 3 3l1.2-1 2 2-1.3 1.6C4.5 9 1 5.5.6 1.8z"/></svg> +43 1 5849162
      <svg viewBox="0 0 10 10"><path d="M2.5 0h5v2.5h-5zM0 3h10v5H8v2H2V8H0zM3 6v3h4V6z"/></svg> +43 1 5849163
      <svg viewBox="0 0 10 10"><path d="M0 1.5h10v7H0zM1 2.5l4 3 4-3z" fill-rule="evenodd"/></svg> info@pfotenhaus-demo.at
      <svg viewBox="0 0 10 10"><circle cx="5" cy="5" r="4.5"/></svg> www. pfotenhaus-demo.at
    </div>
    <div>Sparkasse Hollental Nord, &nbsp;| IBAN: AT 58 1111 2222 3333 4444, | BIC: HLNTAT2H517</div>
  </footer>

  <div class="band"></div>
</div>
</body>
</html>
```